Flyer-Design für Fahrschule
Zielgruppe
Autofahrschule
18-22 jährige
Aufgabenstellung
A5 ein oder zweiseitig
Design: jung, popig, modern, ansprechend,
Fotos von mir mit Vornamen und ein Foto von Auto evtl auch zusätzlich passende Stockbilder, Logo, gleiches Blau wie im Logo verwenden
Text: 076 914 58 27 kurvenprofi.ch (ev. jung - dynamisch - kompetent) ... will Träum chönd wahr werde !!
Gutschein für 1 Fahrstunde integrieren.

```html
<!DOCTYPE html>
<html lang="de">
<head>
<meta charset="UTF-8">
<title>Kurvenprofi Fahrschule – Flyer</title>
<link href="https://fonts.googleapis.com/css2?family=Audiowide&family=Montserrat:ital,wght@0,400;0,600;0,800;1,800&display=swap" rel="stylesheet">
<style>
  :root{
    --brand-blue:#2b27b0;
    --deep-blue:#1a1480;
    --silver:#b9bcc2;
    --ink:#1b1b1b;
    --grey:#555;
    --paper:#ffffff;
    --backdrop:#e6e7ea;
  }
  *{margin:0;padding:0;box-sizing:border-box}
  html,body{width:1200px;height:960px;overflow:hidden;background:var(--backdrop)}
  .flyer{
    position:absolute;left:285px;top:35px;width:630px;height:890px;
    background:var(--paper);overflow:hidden;
    box-shadow:0 6px 24px rgba(0,0,0,.18);
    font-family:"Montserrat",sans-serif;
  }
  .hero-photo{
    position:absolute;left:0;top:0;width:630px;height:370px;
    background:linear-gradient(180deg,#6fa9e0 0%,#bcd8f0 45%,#9fb7a0 70%,#6f8f5a 100%);
  }
  .hero-cut{position:absolute;left:0;top:0;width:630px;height:420px}
  .brand-name{
    position:absolute;left:30px;top:30px;
    font-weight:800;font-size:26px;line-height:1;color:var(--paper);
  }
  .phone{
    position:absolute;left:0;right:34px;top:388px;text-align:right;
    font-family:"Audiowide",sans-serif;font-size:60px;color:var(--brand-blue);line-height:1;
  }
  .domain{
    position:absolute;left:0;right:30px;top:450px;text-align:right;
    font-family:"Audiowide",sans-serif;font-size:64px;line-height:1;
    color:var(--silver);letter-spacing:1px;
  }
  .claim{
    position:absolute;left:0;right:34px;top:525px;text-align:right;
    font-size:17px;letter-spacing:5px;color:var(--grey);
  }
  .slogan{
    position:absolute;left:0;right:34px;top:556px;text-align:right;
    font-weight:800;font-style:italic;font-size:26px;color:var(--brand-blue);
  }
  .slogan .dark{color:var(--ink)}
  .voucher{position:absolute;left:0;top:600px;width:630px;height:290px}
  .voucher-band{position:absolute;inset:0}
  .keys{
    position:absolute;right:18px;top:0;width:150px;height:120px;border-radius:40px 10px 40px 10px;
    background:radial-gradient(circle at 40% 45%,#3a3a3a,#111 70%);
  }
  .voucher-title{
    position:absolute;left:40px;top:128px;
    font-family:"Audiowide",sans-serif;font-size:80px;line-height:1;color:var(--silver);
  }
  .voucher-sub{
    position:absolute;left:44px;top:212px;font-size:15px;font-weight:600;letter-spacing:3px;color:#dfe0ff;
  }
  .voucher-sub b{font-weight:800;color:#fff}
  .voucher-web{
    position:absolute;left:44px;top:242px;display:flex;align-items:center;gap:16px;
    font-family:"Audiowide",sans-serif;font-size:20px;color:#fff;
  }
  .dot{width:20px;height:20px;border:2px solid #fff;border-radius:50%}
</style>
</head>
<body>
<main class="flyer">
  <div class="hero-photo" role="img" aria-label="Foto des Fahrlehrers neben dem weissen Fahrschulauto unter blauem Himmel"></div>
  <svg class="hero-cut" viewBox="0 0 630 420" aria-hidden="true">
    <polygon points="0,330 150,300 230,370 330,290 420,300 630,200 630,420 0,420" fill="#ffffff"/>
    <polygon points="230,370 330,290 360,300 260,380" fill="#d7dbe2"/>
  </svg>
  <div class="brand-name">kurvenprofi.ch</div>

  <div class="phone">076 914 58 27</div>
  <div class="domain">kurvenprofi.ch</div>
  <div class="claim">JUNG - DYNAMISCH - UNKOMPLIZIERT</div>
  <div class="slogan">...will Träum chönd <span class="dark">wahr werde</span></div>

  <section class="voucher">
    <svg class="voucher-band" viewBox="0 0 630 290" preserveAspectRatio="none" aria-hidden="true">
      <defs>
        <linearGradient id="bandShade" x1="0" y1="0" x2="1" y2="1">
          <stop offset="0" stop-color="#3b35c8"/>
          <stop offset="1" stop-color="#1a1480"/>
        </linearGradient>
      </defs>
      <polygon points="0,290 0,150 60,80 380,80 430,20 470,20 470,0 630,0 630,290" fill="url(#bandShade)"/>
    </svg>
    <div class="keys" role="img" aria-label="Autoschlüssel mit Funkfernbedienung"></div>
    <div class="voucher-title">Gutschein</div>
    <div class="voucher-sub"><b>FÜR 1 FAHRSTUNDE</b> INTEGRIEREN</div>
    <div class="voucher-web">www.kurvenprofi.ch <span class="dot"></span><span class="dot"></span></div>
  </section>
</main>
</body>
</html>
```